The logo name is "Harbon Vellis". The name of the product will be "Tavoren Calm". This product is specifically formulated for amputees. Therefore under the product name it should state "for amputees". The catch phrase will be "Experience Harbon gain Wellstride"
These are the things we need on the label:
Logo, product name, "for amputees", "Experience Harbon gain Wellstride", Safe, Effective, Directions: spray on problem areas, no need to dry off. harbonvellis.example, Made in Canada, 500ml.
The MOST IMPORTANT and therefore the most prominent thing on this lable will be the LOGO! The second most prominent thing will be the word "Calm" We want to keep it very plain, very simple, very unclutered. Keep in mind that this lable will be placed on a white bottle or have a white back ground. The 500ml white PE bottle with trigger sprayer will have a tear drop label. See attached die line (S-294).
We want to stay with the colours that goes with the colour scheme of the logo. See attached logo. Soft colours. We do not want a picture! We would like the lable to be classy and rich.
Updates
The logo name is "Harbon Vellis". The name of the product will be "Tavoren Calm". This product is specificlly formulated for amputees. Therefore under the product name it should state "for amputees". The catch phrase will be "Experience Harbon gain Wellstride"
Logo, product name, "for amputees", catch phrase "Experience Harbon gain Wellstride", Clean, Safe, Effective, Directions: spray on problem areas, no need to dry off. Also Harbon Vellis Corpation, harbonvellis.example, Made in Canada, 500ml.
We want to stay with the colour scheme of the logo. See attached logo. Soft colours. We do not want a picture! We would like the lable to be classy and rich.
This is the offical directive that came from the governing panal of this lable. This panal it not know where it wanted to take this lable that would represent this line until they review all of your submissions, thank you for all your talented hard work. But now it is clear it is time to regroup and hit this objective.
Target Market(s)
Amputees and Parents of.
Industry/Entity Type
Product
Requirements
Must have
- Final product to be in a pdf or an illustrator file

```html
<!DOCTYPE html>
<html lang="en">
<head>
<meta charset="utf-8">
<title>Harbon Vellis – Tavoren Calm Label</title>
<link rel="stylesheet" href="https://fonts.googleapis.com/css2?family=Cinzel:wght@700;900&family=Libre+Baskerville:wght@700&family=Roboto+Condensed:ital,wght@0,400;0,700;1,700&display=swap">
<style>
  :root {
    --page: #ededed;
    --mint: #cfeae7;
    --mint-soft: #e8f5f3;
    --white: #ffffff;
    --teal: #33aaa1;
    --teal-deep: #1d6f6a;
    --gold: #f6b84a;
    --gold-light: #fbd27a;
    --gold-dark: #a8641c;
    --ink: #2b3b3a;
  }
  * { margin: 0; padding: 0; box-sizing: border-box; }
  html, body { width: 1200px; height: 1000px; overflow: hidden; background: var(--page); }
  .canvas { position: relative; width: 1200px; height: 1000px; }
  .label { position: absolute; left: 330px; top: 50px; width: 540px; height: 900px; }
  .label-shape { position: absolute; inset: 0; width: 540px; height: 900px; }
  .label-content { position: absolute; inset: 0; text-align: center; font-family: "Roboto Condensed", sans-serif; color: var(--ink); }

  .brand { position: absolute; top: 160px; left: 0; right: 0; display: flex; justify-content: center; align-items: center; gap: 16px; }
  .brand-mark { width: 46px; height: 46px; background: var(--teal); }
  .brand-name { font-family: "Libre Baskerville", serif; font-weight: 700; font-size: 44px; color: var(--teal-deep); }

  .product-line { position: absolute; top: 354px; left: 0; right: 0; font-size: 30px; letter-spacing: 6px; color: var(--white); line-height: 1; }
  .product-name {
    position: absolute; top: 390px; left: 0; right: 0;
    font-family: "Cinzel", serif; font-weight: 900; font-size: 106px; line-height: 1; letter-spacing: 6px;
    color: var(--gold-light);
    text-shadow:
      1.5px 0 0 var(--gold-dark), -1.5px 0 0 var(--gold-dark),
      0 1.5px 0 var(--gold-dark), 0 -1.5px 0 var(--gold-dark),
      1px 1px 0 var(--gold-dark), -1px -1px 0 var(--gold-dark),
      1px -1px 0 var(--gold-dark), -1px 1px 0 var(--gold-dark),
      2px 3px 4px rgba(0, 0, 0, 0.25);
  }
  .audience { position: absolute; top: 500px; left: 0; right: 0; color: var(--white); line-height: 1; }
  .audience-for { display: block; font-size: 22px; font-weight: 700; }
  .audience-who { display: block; font-size: 42px; font-weight: 700; font-style: italic; letter-spacing: 1px; margin-top: 2px; }

  .tagline { position: absolute; top: 600px; left: 0; right: 0; font-size: 29px; font-weight: 700; color: var(--teal-deep); }
  .claims {
    position: absolute; top: 648px; left: 160px; width: 220px; padding: 6px 0;
    background: var(--teal); border: 3px solid var(--teal); outline: 2px solid var(--white); outline-offset: -7px;
    font-family: "Libre Baskerville", serif; font-size: 19px; line-height: 1.2; color: var(--white);
  }
  .directions { position: absolute; top: 740px; left: 0; right: 0; font-size: 13px; line-height: 1.25; color: var(--teal-deep); font-weight: 700; }
  .directions-title { font-style: italic; display: block; }
  .maker { position: absolute; top: 784px; left: 0; right: 0; font-size: 13px; line-height: 1.25; font-weight: 700; color: var(--teal-deep); }
  .maker-title { font-style: italic; display: block; }
  .website { position: absolute; top: 828px; left: 0; right: 0; font-size: 14px; font-weight: 700; letter-spacing: 4px; color: var(--teal-deep); }
  .origin { position: absolute; top: 858px; left: 0; right: 0; font-size: 13px; font-weight: 700; color: var(--teal-deep); }
</style>
</head>
<body>
<main class="canvas">
  <section class="label">
    <svg class="label-shape" viewBox="0 0 540 900" aria-hidden="true">
      <defs>
        <linearGradient id="label-fill" x1="0" y1="0" x2="0" y2="1">
          <stop offset="0" stop-color="#bfe3df"/>
          <stop offset="0.3" stop-color="#f4fbfa"/>
          <stop offset="0.62" stop-color="#ffffff"/>
          <stop offset="1" stop-color="#cfeae7"/>
        </linearGradient>
        <linearGradient id="band-fill" x1="0" y1="0" x2="0" y2="1">
          <stop offset="0" stop-color="#2fa69d"/>
          <stop offset="0.5" stop-color="#45b8ae"/>
          <stop offset="1" stop-color="#2a9e96"/>
        </linearGradient>
        <clipPath id="label-clip">
          <path d="M20 240 C20 120 95 62 215 52 L440 30 C500 25 528 62 528 112 L528 862 Q528 896 494 896 L46 896 Q12 896 12 862 Z"/>
        </clipPath>
      </defs>
      <path class="label-body" d="M20 240 C20 120 95 62 215 52 L440 30 C500 25 528 62 528 112 L528 862 Q528 896 494 896 L46 896 Q12 896 12 862 Z" fill="url(#label-fill)"/>
      <g clip-path="url(#label-clip)">
        <path class="band-gold" d="M0 388 C150 318 380 308 540 340 L540 530 C380 592 160 612 0 598 Z" fill="#f6b84a"/>
        <path class="band-teal" d="M0 398 C150 330 380 320 540 350 L540 520 C380 580 160 600 0 588 Z" fill="url(#band-fill)"/>
      </g>
    </svg>

    <div class="label-content">
      <div class="brand">
        <span class="brand-mark"></span>
        <span class="brand-name">Harbon Vellis</span>
      </div>

      <p class="product-line">Tavoren</p>
      <h1 class="product-name">CALM</h1>
      <p class="audience"><span class="audience-for">For</span><span class="audience-who">AMPUTEES</span></p>

      <p class="tagline">Experience Harbon gain Wellstride</p>
      <p class="claims">CLEAN, SAFE<br>&amp; EFFECTIVE</p>

      <p class="directions"><span class="directions-title">Directions:</span>Spray on problem areas, no need to dry off.</p>
      <p class="maker"><span class="maker-title">Manufactured by:</span>Harbon Vellis Corpation</p>
      <p class="website">www.harbonvellis.example</p>
      <p class="origin">Made in Canada &nbsp;|&nbsp; 500mL</p>
    </div>
  </section>
</main>
</body>
</html>
```